Refresh of Business Card Design

Want to refresh the business card design with the new logo while adhering to style guide as attached. Would like to match feel of website www.brimwickdrives.com

```html
<!DOCTYPE html>
<html lang="en">
<head>
<meta charset="utf-8">
<title>Brimwick Drives – Business Card</title>
<link href="https://fonts.googleapis.com/css2?family=Open+Sans:wght@400;700&display=swap" rel="stylesheet">
<style>
  :root {
    --stage: #3b3b3b;
    --card: #151515;
    --accent: #e3262b;
    --text: #e8e8e8;
    --muted: #cfcfcf;
  }
  * { box-sizing: border-box; margin: 0; padding: 0; }
  html, body { width: 1200px; height: 801px; overflow: hidden; }
  body {
    background: var(--stage);
    font-family: "Open Sans", Arial, sans-serif;
    position: relative;
  }
  .card {
    position: absolute;
    top: 246px;
    width: 540px;
    height: 309px;
    background: var(--card);
    border: 2px solid var(--accent);
  }
  .card--front { left: 40px; }
  .card--back { left: 620px; }

  .brand {
    position: absolute;
    display: flex;
    align-items: center;
    gap: 10px;
    color: var(--text);
    font-weight: 400;
    text-transform: uppercase;
    letter-spacing: 0.04em;
    white-space: nowrap;
  }
  .brand__dot {
    border-radius: 50%;
    background: var(--accent);
    flex: none;
  }
  .card--front .brand { right: 34px; top: 52px; font-size: 17px; }
  .card--front .brand__dot { width: 22px; height: 22px; }
  .card--back .brand {
    left: 50%; top: 50%;
    transform: translate(-50%, -50%);
    font-size: 30px;
    gap: 16px;
  }
  .card--back .brand__dot { width: 40px; height: 40px; }

  .divider {
    position: absolute;
    left: 34px; right: 34px; top: 170px;
    height: 1px;
    background: var(--accent);
  }
  .person { position: absolute; left: 34px; top: 122px; }
  .person__name {
    color: var(--accent);
    font-weight: 700;
    font-size: 19px;
    letter-spacing: 0.02em;
    text-transform: uppercase;
    line-height: 1.1;
  }
  .person__role { color: var(--muted); font-size: 12px; margin-top: 2px; }

  .contact {
    position: absolute; left: 34px; top: 190px;
    list-style: none;
    color: var(--text);
    font-size: 12px;
    line-height: 20px;
  }
  .contact li { display: flex; align-items: center; gap: 8px; }
  .contact svg { width: 11px; height: 11px; fill: var(--accent); flex: none; }

  .address {
    position: absolute; right: 34px; top: 190px;
    color: var(--text);
    font-size: 12px;
    line-height: 20px;
    font-style: normal;
  }
</style>
</head>
<body>
  <section class="card card--front">
    <div class="brand"><span class="brand__dot"></span>Brimwick Drives</div>
    <div class="person">
      <p class="person__name">Dana Merrow</p>
      <p class="person__role">Sales</p>
    </div>
    <div class="divider"></div>
    <ul class="contact">
      <li><svg viewBox="0 0 12 12" aria-hidden="true"><path d="M2.5 0.8 4.4 3 3.4 4.3c.7 1.6 2.2 3.1 3.8 3.8l1.3-1 2.2 1.9-1 1.9C5.5 10.6 1.4 6.5.6 2.3z"/></svg>555.014.2876</li>
      <li><svg viewBox="0 0 12 12" aria-hidden="true"><path d="M0 2.5h12v7H0z M0.6 3 6 6.8 11.4 3" stroke="#151515" stroke-width="0.9"/></svg>dmerrow@brimwickdrives.com</li>
      <li><svg viewBox="0 0 12 12" aria-hidden="true"><circle cx="6" cy="6" r="5.5"/></svg>www.brimwickdrives.com</li>
    </ul>
    <address class="address">
      P.O. Box 40218 Larkfield, TX 79034<br>
      48 Harlow Ln Fenton, Texas 79152
    </address>
  </section>

  <section class="card card--back">
    <div class="brand"><span class="brand__dot"></span>Brimwick Drives</div>
  </section>
</body>
</html>
```